Business Card, Stationary, Brochure Template, Flyer Template
Templates need to be provided in Microsoft Publisher format as well as industry standards
Business Card, Stationary, Brochure Template, Flyer Template - Entertainment
Creative Brief
Use specific fonts
Font choice up to designer
Professional
Martin Hollowes
Managing Director
Unit Farrowby B Elmstead Court Redgate Lane Ashcombe St Peter Wiltshire SN14 8QT, UK
martin.hollowes@brightquill.co.uk
www.brightquill.co.uk
The Business cards designs need to be to the UK standard size 90cm by 55cm not the US standard shown in the brief. The business cards and Stationary need to have our company logo. The Brochure and Flyer template need to work with both our company logo and our product logo. For the Brochure and Flyer templates we are looking for a design that works along with our Stationary, we only require a template design something like these http://www.pagemoldery.com/Templates/Free-Templates/Free-Sample-Brochure-Template-Design.aspx and http://www.pagemoldery.com/Templates/Free-Templates/Free-Sample-Flyer-Template-Design.aspx but obviously unique to us and matching the other designs.

```html
<!DOCTYPE html>
<html lang="en">
<head>
<meta charset="utf-8">
<title>brightquill stationery and templates</title>
<link rel="stylesheet" href="https://fonts.googleapis.com/css2?family=Open+Sans:wght@400;600;700&display=swap">
<style>
:root{
  --red:#d4252c;
  --green:#3aa645;
  --blue:#2a6db5;
  --teal:#1f8fb0;
  --ink:#111111;
  --text:#555555;
  --paper:#ffffff;
  --rule:#cfcfcf;
  --band-top:#e9e9ee;
  --band-bottom:#1a1a22;
}
*{box-sizing:border-box;margin:0;padding:0}
html,body{width:1200px;height:626px;overflow:hidden;background:#fff}
body{font-family:"Open Sans",Arial,sans-serif;color:var(--text)}
.sheet{position:relative;width:1200px;height:626px;overflow:hidden;background:#fff}
.item{position:absolute;background:var(--paper);box-shadow:0 0 0 1px #e3e3e3;overflow:hidden}
.band{position:absolute;left:0;width:100%;background:linear-gradient(180deg,var(--band-top),var(--band-bottom))}
.brand{position:absolute;font-weight:700;color:var(--ink);letter-spacing:-.3px;display:flex;align-items:center;gap:4px;white-space:nowrap}
.brand i{display:inline-block;background:var(--red)}
.photo{position:absolute}
.panel{position:absolute;top:0;height:100%}
.tiny{font-size:4.6px;line-height:6.4px}
.h-red{color:var(--red);font-weight:700;text-transform:uppercase}
.h-dark{color:var(--ink);font-weight:700;text-transform:uppercase}
.tagline{display:flex;gap:6px;align-items:center}
.tagline .dot{width:12px;height:12px;border-radius:50%;background:var(--red);flex:none}
.tagline span:last-child{font-size:6px;line-height:8px}
ul.ticks{list-style:none}
ul.ticks li::before{content:"\2713 ";color:var(--green);font-weight:700}
.card{position:absolute;width:78px;height:42px;padding:6px}
.card .brand{position:static;font-size:9px;color:#fff}
.form-table{border-collapse:collapse;width:100%}
.form-table td{border:1px solid var(--rule);font-size:5px;padding:2px 3px;height:11px;color:var(--ink)}
.checks{display:flex;gap:6px;font-size:4.6px;color:var(--ink)}
.checks span::before{content:"";display:inline-block;width:4px;height:4px;border:1px solid var(--ink);margin-right:2px;vertical-align:-1px}
</style>
</head>
<body>
<main class="sheet">

  <!-- Brochure outer spread -->
  <section class="item brochure-outer" style="left:5px;top:5px;width:500px;height:295px">
    <div class="photo" role="img" aria-label="Nightclub stage with coloured beams of light" style="left:0;top:0;width:250px;height:110px;background:radial-gradient(circle at 55% 40%,#6a3fb0,#1b1440 55%,#07050f)"></div>
    <div style="position:absolute;left:0;top:110px;width:250px;height:72px;background:var(--ink);padding:8px 10px;color:#ddd">
      <div style="width:14px;height:14px;border-radius:50%;background:var(--red);position:absolute;left:10px;top:10px"></div>
      <div style="position:absolute;left:120px;top:8px;width:110px">
        <div class="tiny" style="color:#fff;font-weight:700">Head Office</div>
        <p class="tiny">Unit Farrowby B Elmstead Court Redgate Lane Ashcombe St Peter Wiltshire SN14 8QT</p>
        <p class="tiny" style="margin-top:3px">martin.hollowes@brightquill.co.uk</p>
        <p class="tiny">www.brightquill.co.uk</p>
      </div>
    </div>
    <div class="band" role="img" aria-label="Decorative coloured wave band" style="top:182px;height:28px;width:250px"></div>
    <div class="brand" style="left:120px;top:226px;font-size:14px"><i style="width:9px;height:9px"></i>brightquill</div>
    <p class="tiny" style="position:absolute;left:120px;top:248px;width:110px">Unit Farrowby B Elmstead Court Redgate Lane Ashcombe St Peter Wiltshire SN14 8QT</p>

    <div class="panel" style="left:250px;width:250px;padding:8px 10px">
      <div class="tagline"><span class="dot"></span><span class="h-red">Intelligent Colour Control<br>&amp; Lighting Systems</span></div>
    </div>
    <div class="photo" role="img" aria-label="DJ performing at a mixing desk under blue stage lights" style="left:250px;top:32px;width:250px;height:168px;background:linear-gradient(160deg,#1c2b6b,#0a0f2a 60%,#3b1c5e)"></div>
    <div class="band" role="img" aria-label="Decorative coloured wave band" style="left:250px;top:200px;height:30px;width:250px"></div>
    <div class="brand" style="left:312px;top:252px;font-size:20px"><i style="width:12px;height:12px"></i>brightquill</div>
  </section>

  <!-- Business cards -->
  <div class="card" style="left:533px;top:7px;background:var(--red)"><div class="brand">brightquill</div></div>
  <div class="card" style="left:617px;top:7px;background:var(--blue)"><div class="brand">brightquill</div></div>
  <div class="card" style="left:533px;top:53px;background:var(--green)"><div class="brand">brightquill</div></div>
  <div class="card" style="left:617px;top:53px;background:var(--teal)"><div class="brand">brightquill</div></div>

  <!-- Letterhead -->
  <section class="item letterhead" style="left:703px;top:7px;width:156px;height:228px">
    <div class="brand" style="left:10px;top:16px;font-size:11px"><i style="width:7px;height:7px"></i>brightquill</div>
    <div class="tiny" style="position:absolute;right:8px;top:10px;width:62px;text-align:right;font-size:3.6px;line-height:5px">
      <b style="color:var(--ink)">Martin Hollowes</b><br>Unit Farrowby B Elmstead Court Redgate Lane Ashcombe St Peter Wiltshire SN14 8QT<br>martin.hollowes@brightquill.co.uk<br>www.brightquill.co.uk
    </div>
    <div class="band" role="img" aria-label="Decorative coloured wave band" style="top:200px;height:28px"></div>
  </section>

  <!-- Envelope DL -->
  <section class="item envelope" style="left:533px;top:100px;width:164px;height:125px">
    <div class="tiny" style="position:absolute;left:8px;top:8px;width:80px;font-size:3.6px;line-height:5px">Unit Farrowby B Elmstead Court Redgate Lane Ashcombe St Peter Wiltshire SN14 8QT</div>
    <div class="brand" style="left:56px;top:56px;font-size:11px"><i style="width:7px;height:7px"></i>brightquill</div>
    <div class="band" role="img" aria-label="Decorative coloured wave band" style="top:100px;height:25px"></div>
  </section>

  <!-- Flyer front -->
  <section class="item flyer-front" style="left:960px;top:7px;width:230px;height:293px">
    <div class="tagline" style="padding:8px 10px"><span class="dot"></span><span class="h-red">Intelligent Colour Control<br>&amp; Lighting Systems</span></div>
    <div class="photo" role="img" aria-label="DJ performing at a mixing desk under blue stage lights" style="left:0;top:34px;width:230px;height:170px;background:linear-gradient(160deg,#1c2b6b,#0a0f2a 60%,#3b1c5e)"></div>
    <div class="band" role="img" aria-label="Decorative coloured wave band" style="top:204px;height:28px"></div>
    <div class="brand" style="left:52px;top:248px;font-size:19px"><i style="width:11px;height:11px"></i>brightquill</div>
  </section>

  <!-- Brochure inside spread -->
  <section class="item brochure-inside" style="left:5px;top:312px;width:500px;height:308px">
    <div class="panel" style="left:0;width:167px;padding:8px 9px">
      <div class="h-red" style="font-size:6.5px">Introduction</div>
      <p class="tiny">Smart lighting control for clubs, venues and touring shows, built to be simple and reliable every night.</p>
      <div class="photo" role="img" aria-label="Coloured stage lights over a dance floor" style="left:95px;top:30px;width:62px;height:36px;background:linear-gradient(135deg,#2a3a8c,#0c0c24)"></div>
      <div class="h-red" style="font-size:6.5px;margin-top:44px">Products</div>
      <div class="photo" role="img" aria-label="Purple lit lighting fixture" style="left:9px;top:92px;width:70px;height:50px;background:radial-gradient(circle,#b14be0,#2a0c45 70%)"></div>
    </div>
    <div class="panel" style="left:167px;width:167px;padding:8px 9px">
      <div class="h-red" style="font-size:6.5px">Technology that reacts to sound</div>
      <p class="tiny">Every fixture reads the room and adjusts colour in real time.</p>
      <div class="photo" role="img" aria-label="Crowd and stage under red and blue lights" style="left:9px;top:30px;width:149px;height:50px;background:linear-gradient(120deg,#6a1020,#101030 55%,#1d3f8a)"></div>
      <ul class="ticks tiny" style="margin-top:62px;margin-left:60px">
        <li>Fast setup</li><li>Wireless control</li><li>Low power use</li><li>Full colour range</li><li>Remote support</li>
      </ul>
    </div>
    <div class="photo" role="img" aria-label="Silhouetted concert crowd with raised hands against bright stage light" style="left:0;top:190px;width:334px;height:118px;background:linear-gradient(180deg,#f2f2f2 0%,#9a9a9a 35%,#111 70%)"></div>
    <div class="panel" style="left:334px;width:166px;padding:8px 9px">
      <div class="h-red" style="font-size:6.5px">Why choose us</div>
      <p class="tiny">Designed and built in Britain with support from a team that knows live events.</p>
      <div class="h-red" style="font-size:6.5px;margin-top:8px">Get in touch</div>
      <p class="tiny">Unit Farrowby B Elmstead Court Redgate Lane Ashcombe St Peter Wiltshire SN14 8QT<br>martin.hollowes@brightquill.co.uk<br>www.brightquill.co.uk</p>
    </div>
    <div class="photo" role="img" aria-label="Bridge lit with coloured lights at night" style="left:334px;top:150px;width:166px;height:158px;background:linear-gradient(180deg,#3b2a1a,#8a5a20 45%,#1a1208)"></div>
  </section>

  <!-- Envelope C5 -->
  <section class="item envelope-large" style="left:533px;top:372px;width:167px;height:193px">
    <div class="tiny" style="position:absolute;left:8px;top:8px;width:80px;font-size:3.6px;line-height:5px">Unit Farrowby B Elmstead Court Redgate Lane Ashcombe St Peter Wiltshire SN14 8QT</div>
    <div class="brand" style="left:56px;top:64px;font-size:11px"><i style="width:7px;height:7px"></i>brightquill</div>
    <div class="band" role="img" aria-label="Decorative coloured wave band" style="top:92px;height:30px"></div>
  </section>

  <!-- Fax form -->
  <section class="item fax-form" style="left:708px;top:324px;width:152px;height:252px;padding:10px 9px">
    <div class="brand" style="position:static;font-size:10px"><i style="width:6px;height:6px"></i>brightquill</div>
    <div class="h-dark" style="font-size:8px;margin:10px 0 4px">Fax</div>
    <table class="form-table">
      <tr><td>To</td><td></td><td>From</td><td></td></tr>
      <tr><td>Fax</td><td></td><td>Pages</td><td></td></tr>
      <tr><td>Date</td><td></td><td>Re</td><td></td></tr>
    </table>
    <div class="checks" style="margin-top:6px"><span>Urgent</span><span>Review</span><span>Reply</span><span>Comment</span></div>
    <div class="band" role="img" aria-label="Decorative coloured wave band" style="top:222px;height:30px"></div>
  </section>

  <!-- Flyer back -->
  <section class="item flyer-back" style="left:960px;top:312px;width:230px;height:308px;padding:9px 10px">
    <div class="h-red" style="font-size:7px">Benefits</div>
    <p class="tiny" style="width:130px">Cut setup time and give every show a clear, bright look that guests remember.</p>
    <div class="photo" role="img" aria-label="Band on stage under coloured lights" style="left:10px;top:42px;width:210px;height:62px;background:linear-gradient(120deg,#7a1830,#151538 55%,#2a5aa8)"></div>
    <div class="h-red" style="font-size:7px;margin-top:82px">Environmentally aware lighting</div>
    <p class="tiny" style="width:130px">Lower energy use with no loss of colour or output.</p>
    <div class="photo" role="img" aria-label="Lighting rig above a stage" style="left:150px;top:122px;width:70px;height:52px;background:linear-gradient(135deg,#2a2a5a,#0a0a1a)"></div>
    <div class="brand" style="left:60px;top:214px;font-size:16px"><i style="width:10px;height:10px"></i>brightquill</div>
    <div class="band" role="img" aria-label="Decorative coloured wave band" style="top:276px;height:32px"></div>
  </section>

</main>
</body>
</html>
```